A4 Flyer to launch franchise accounting service

We are an Australian bookkeeping business specialising in servicing the national franchise industry. We don't want to look like just another bookkeeper ... we want an element of coolness in the design - but not too gimmicky.

The draft wording and notes are in the attached file - please source relevant images as appropriate. It is somewhat wordy so please layout the wording so it is not all in one vertical column.

Target Market(s)

Franchisors

Industry/Entity Type

Finance

Font styles to use
Sans Serif

Requirements
Must have
• Headline: Is there a piece missing from your franchise model?
• NB: Our logo is not to take centre stage.
Nice to have
• Images that reflect our message could be similar to the following (please utilise better images if you have any - these are a guide only):
• http://ledgerwisp.example.com.au/wp-content/uploads/2015/08/Cloud-accounting-software.jpg
• http://www.tmvtradingagents.example.com.au/wp-content/uploads/2015/08/Franchised-Business.jpg
• https://www.harlinvo.example.org/wp/wp-content/uploads/2014/04/mb-reason-1.gif
• https://gwenpalister.files.example-blogs.com/2013/03/benchmarking.png
Should not have
• Look of a boring bookkeeper/accountant.

```html
<!DOCTYPE html>
<html lang="en">
<head>
<meta charset="utf-8">
<title>Crestline Bookkeeping – Franchise Flyer</title>
<link href="https://fonts.googleapis.com/css2?family=Rajdhani:wght@500;600;700&family=Titillium+Web:wght@400;600&display=swap" rel="stylesheet">
<style>
  :root{
    --teal:#2a9aa3;
    --teal-dark:#1d7d86;
    --cyan:#3fd0e0;
    --navy:#1b2a5c;
    --ink:#2b3a63;
    --white:#ffffff;
    --paper:#f4f8fa;
    --grey-logo:#e9ecee;
    --bg:#e6e8ea;
  }
  *{box-sizing:border-box;margin:0;padding:0}
  html,body{width:1200px;height:849px;overflow:hidden;background:var(--bg)}
  body{font-family:"Titillium Web",sans-serif;position:relative}
  .flyer{position:absolute;left:317px;top:24px;width:566px;height:800px;background:var(--white);overflow:hidden;box-shadow:0 4px 18px rgba(0,0,0,.25)}
  .logo-panel{position:absolute;left:0;top:0;width:178px;height:142px;background:linear-gradient(180deg,#fff,var(--grey-logo));display:flex;flex-direction:column;align-items:center;justify-content:center;gap:12px;z-index:2}
  .logo-square{width:34px;height:34px;background:var(--teal)}
  .logo-name{font-family:"Rajdhani",sans-serif;font-weight:600;font-size:17px;color:var(--navy);white-space:nowrap}
  .header{position:absolute;left:178px;top:0;right:0;height:134px;background:var(--teal);color:var(--white);padding:12px 16px 0 18px}
  .headline{font-family:"Rajdhani",sans-serif;font-weight:700;font-size:21px;line-height:1.05;text-transform:uppercase;margin-bottom:8px}
  .intro{font-size:7.4px;line-height:1.35;margin-bottom:5px}
  .hero{position:absolute;left:0;top:134px;width:566px;height:272px;background:radial-gradient(ellipse at 58% 40%,#5d7fb0 0%,#243e78 35%,#0d1b40 80%)}
  .sidebar{position:absolute;left:0;top:370px;width:229px;height:430px;background:var(--teal)}
  .hex{position:absolute;left:10px;top:38px}
  .services{position:absolute;left:46px;top:94px;list-style:none;color:var(--white);font-family:"Rajdhani",sans-serif;font-weight:600;font-size:12.5px}
  .services li{display:flex;align-items:center;gap:5px;height:20px;white-space:nowrap}
  .services svg{flex:none}
  .partner{position:absolute;left:46px;top:252px;display:flex;align-items:center;gap:9px;color:var(--white)}
  .partner-circle{width:40px;height:40px;border-radius:50%;background:var(--cyan);border:2px solid var(--white);flex:none}
  .partner-text{font-size:9.5px;line-height:1.25}
  .partner-name{font-family:"Rajdhani",sans-serif;font-weight:700;font-size:12px;line-height:1.1;display:block}
  .contact{position:absolute;left:0;top:313px;width:229px;height:78px;background:var(--cyan);padding:14px 0 0 20px;list-style:none;color:var(--navy);font-size:11px}
  .contact li{display:flex;align-items:center;gap:6px;height:17px;white-space:nowrap}
  .main{position:absolute;left:229px;top:406px;width:337px;height:394px;background:var(--paper)}
  .section-bar{background:var(--teal);color:var(--white);font-family:"Rajdhani",sans-serif;font-weight:700;font-size:12px;text-transform:uppercase;padding:2px 12px;height:19px;white-space:nowrap}
  .copy{padding:7px 14px 5px 13px;font-size:7.8px;line-height:1.4;color:var(--ink)}
  .copy p{margin-bottom:6px}
  .benefits{list-style:none;padding:8px 36px 0 13px;color:var(--ink);font-size:9px;line-height:1.3}
  .benefits li{display:flex;gap:6px;margin-bottom:8px}
  .benefits svg{flex:none;margin-top:2px}
  .footer-strip{position:absolute;left:229px;bottom:0;width:337px;height:8px;background:var(--navy)}
</style>
</head>
<body>
<div class="flyer">
  <div class="logo-panel">
    <div class="logo-square"></div>
    <div class="logo-name">Crestline Bookkeeping</div>
  </div>

  <header class="header">
    <h1 class="headline">Is there a piece missing from<br>your franchise model?</h1>
    <p class="intro">Franchising is about replicating and selling a proven business model. Yet when it comes to accounting, each franchisee is often left to their own, leading to inconsistent &amp; unreliable reporting.</p>
    <p class="intro">Crestline Bookkeeping are specialists in franchise performance accounting. Beyond timely and uniform franchisee accounts, our consolidated reporting and benchmark analysis ensures your finger is on the pulse at every level in your franchise.</p>
  </header>

  <div class="hero" role="img" aria-label="Photo of a businessman touching a glowing 'Franchise' button on a virtual screen"></div>

  <svg class="wave" style="position:absolute;left:229px;top:360px" width="337" height="60" viewBox="0 0 337 60" aria-hidden="true">
    <path d="M0 60 L0 40 Q150 50 337 0 L337 60 Z" fill="var(--paper)"/>
    <path d="M0 40 Q150 50 337 0" fill="none" stroke="var(--cyan)" stroke-width="4"/>
    <path d="M0 47 Q150 56 337 8" fill="none" stroke="var(--navy)" stroke-width="3"/>
  </svg>

  <aside class="sidebar">
    <svg class="hex" width="204" height="190" viewBox="0 0 204 190" aria-hidden="true">
      <defs>
        <linearGradient id="sky" x1="0" y1="0" x2="0" y2="1">
          <stop offset="0" stop-color="#3a8fd6"/>
          <stop offset="1" stop-color="#cfe8f7"/>
        </linearGradient>
      </defs>
      <polygon points="50,4 154,4 202,95 154,186 50,186 2,95" fill="var(--cyan)"/>
      <polygon points="54,11 150,11 194,95 150,179 54,179 10,95" fill="var(--navy)"/>
      <polygon points="58,17 146,17 187,95 146,173 58,173 17,95" fill="url(#sky)" role="img" aria-label="Blue sky with clouds"/>
    </svg>
    <ul class="services">
      <li><svg width="13" height="13" viewBox="0 0 13 13"><circle cx="6.5" cy="6.5" r="6.5" fill="var(--navy)"/><rect x="3.5" y="6" width="1.5" height="4" fill="#fff"/><rect x="6" y="4" width="1.5" height="6" fill="#fff"/><rect x="8.5" y="3" width="1.5" height="7" fill="#fff"/></svg>Benchmarking</li>
      <li><svg width="13" height="13" viewBox="0 0 13 13"><circle cx="6.5" cy="6.5" r="6.5" fill="var(--navy)"/><rect x="3.5" y="4" width="6" height="4" fill="#fff"/></svg>Consolidations</li>
      <li><svg width="13" height="13" viewBox="0 0 13 13"><circle cx="6.5" cy="6.5" r="6.5" fill="var(--navy)"/><path d="M3.5 6.8 L5.7 9 L9.6 4.3" stroke="#fff" stroke-width="1.6" fill="none"/></svg>Compliance</li>
      <li><svg width="13" height="13" viewBox="0 0 13 13"><circle cx="6.5" cy="6.5" r="6.5" fill="var(--navy)"/><circle cx="6.5" cy="5" r="2" fill="#fff"/><rect x="3.5" y="7.5" width="6" height="2.5" fill="#fff"/></svg>Franchisee Support</li>
    </ul>
    <div class="partner">
      <div class="partner-circle"></div>
      <div class="partner-text"><span class="partner-name">Ledgerly</span>Beautiful<br>accounting<br>software</div>
    </div>
    <ul class="contact">
      <li><svg width="11" height="11" viewBox="0 0 11 11"><circle cx="5.5" cy="5.5" r="5" fill="none" stroke="var(--navy)"/><path d="M3.5 3 L5 3 L5 4.5 L4.3 5 Q5 6.5 6 6.8 L6.5 6 L8 6 L8 7.5 Q5 8.5 3.5 4.5 Z" fill="var(--navy)"/></svg>1300 555 019</li>
      <li><svg width="11" height="9" viewBox="0 0 11 9"><rect x=".5" y=".5" width="10" height="8" fill="none" stroke="var(--navy)"/><path d="M.5 .5 L5.5 5 L10.5 .5" fill="none" stroke="var(--navy)"/></svg>info@crestline.example.com.au</li>
      <li><svg width="11" height="11" viewBox="0 0 11 11"><circle cx="5.5" cy="5.5" r="5" fill="none" stroke="var(--navy)"/><ellipse cx="5.5" cy="5.5" rx="2" ry="5" fill="none" stroke="var(--navy)"/><line x1=".5" y1="5.5" x2="10.5" y2="5.5" stroke="var(--navy)"/></svg>crestline.example.com.au</li>
    </ul>
  </aside>

  <main class="main">
    <div style="height:24px"></div>
    <h2 class="section-bar">Franchisors … timely information at your fingertips</h2>
    <div class="copy">
      <p>Our highly experienced bookkeepers support your franchisees so their accounts are meaningful, timely &amp; consistent. We provide extra assurance that each franchisee is looking at their financial performance &amp; is compliant with their statutory obligations.</p>
      <p>Our management accountants then breathe new life into these figures via consolidated performance &amp; benchmarking analysis … by region, state and nationally. See who is performing, who needs a hand, and how you're tracking as a group … financially and non-financially.</p>
      <p>Independently prepared, delivered on time … accurate.</p>
      <p>We work nationally to meet the needs of expanding franchises … on the ground and online. Partnering with the services of Ledgerly and leading cloud technology integrators, we deliver a model that enables real-time measurement, business improvement, and even greater head office support.</p>
    </div>
    <h2 class="section-bar">What's in it for franchisees …</h2>
    <ul class="benefits">
      <li><svg width="8" height="8" viewBox="0 0 8 8"><circle cx="4" cy="4" r="3.6" fill="none" stroke="var(--teal)"/><path d="M3 2 L5.4 4 L3 6 Z" fill="var(--teal)"/></svg>Compare your performance monthly to others in the franchise group … quickly see where you can improve.</li>
      <li><svg width="8" height="8" viewBox="0 0 8 8"><circle cx="4" cy="4" r="3.6" fill="none" stroke="var(--teal)"/><path d="M3 2 L5.4 4 L3 6 Z" fill="var(--teal)"/></svg>Easy franchise reporting, BAS &amp; payroll compliance.</li>
      <li><svg width="8" height="8" viewBox="0 0 8 8"><circle cx="4" cy="4" r="3.6" fill="none" stroke="var(--teal)"/><path d="M3 2 L5.4 4 L3 6 Z" fill="var(--teal)"/></svg>Certified Australian bookkeepers managed by experienced accountants… there to do it for you, or someone to fall back on if you DIY.</li>
      <li><svg width="8" height="8" viewBox="0 0 8 8"><circle cx="4" cy="4" r="3.6" fill="none" stroke="var(--teal)"/><path d="M3 2 L5.4 4 L3 6 Z" fill="var(--teal)"/></svg>A partner who comes to intimately know your business to keep you abreast of the important numbers.</li>
    </ul>
  </main>
  <div class="footer-strip"></div>
</div>
</body>
</html>
```